Postcard Design

Marlow Painting-all types of painting and staining-house,deck and roof powerwashing-stone and masonry sealing-
30 years in business-licensed and insured
Ray Pettibone
pettiboneworks@brushmail.example
9145820731

Industry/Entity Type

Painting

```html
<!DOCTYPE html>
<html lang="en">
<head>
<meta charset="utf-8">
<title>Marlow Painting Postcard</title>
<link href="https://fonts.googleapis.com/css2?family=Open+Sans:wght@400;600&display=swap" rel="stylesheet">
<style>
  :root {
    --backdrop: #e2e2e2;
    --paper: #ffffff;
    --ink: #1f1f1f;
    --lilac: #c8b5d8;
    --brand-purple: #a48bbb;
    --panel-black: #161416;
    --panel-text: #e6e6e6;
    --photo-green: #6f8a4e;
    --photo-wood: #9a6b47;
    --strip-frame: #111111;
  }
  * { box-sizing: border-box; margin: 0; padding: 0; }
  html, body { width: 1200px; height: 928px; overflow: hidden; }
  body {
    background: var(--backdrop);
    font-family: "Open Sans", Arial, sans-serif;
    color: var(--ink);
    position: relative;
  }
  .postcard { position: absolute; background: var(--paper); overflow: hidden; box-shadow: 0 1px 4px rgba(0,0,0,.18); }

  /* Address side */
  .postcard--back { left: 85px; top: 393px; width: 576px; height: 439px; z-index: 1; }
  .brand {
    position: absolute; display: flex; align-items: center; gap: 8px;
    color: var(--brand-purple); font-weight: 600; letter-spacing: 1px; white-space: nowrap;
  }
  .brand__mark { background: var(--brand-purple); flex: none; }
  .postcard--back .brand { left: 22px; top: 52px; font-size: 22px; }
  .postcard--back .brand__mark { width: 14px; height: 14px; }
  .tagline { position: absolute; left: 20px; top: 100px; font-size: 13px; }
  .services { list-style: none; position: absolute; }
  .services li { display: flex; align-items: center; gap: 4px; white-space: nowrap; }
  .services svg { flex: none; }
  .postcard--back .services { left: 20px; top: 192px; font-size: 13px; line-height: 19px; }
  .contact { position: absolute; white-space: nowrap; }
  .postcard--back .contact { left: 20px; top: 282px; font-size: 12px; line-height: 17px; }
  .contact__phone { letter-spacing: 1.5px; }
  .postcard--back .contact__phone { font-size: 18px; line-height: 22px; }

  /* Picture side */
  .postcard--front { left: 525px; top: 99px; width: 577px; height: 440px; z-index: 2; }
  .hero {
    position: absolute; left: 0; top: 0; width: 100%; height: 282px;
    background: linear-gradient(100deg, #c9c2b4 0%, #8c6a4f 30%, var(--photo-wood) 50%, var(--photo-green) 75%, #3f5a2c 100%);
  }
  .work-strip {
    position: absolute; left: 6px; top: 275px; width: 434px; height: 93px;
    background: var(--strip-frame); padding: 4px; display: flex; gap: 2px;
  }
  .work-strip__shot { flex: 1; }
  .work-strip__shot:nth-child(1) { background: linear-gradient(#8c7f70, #6e4a38); }
  .work-strip__shot:nth-child(2) { background: linear-gradient(#dfe3e6, #a85b3f); }
  .work-strip__shot:nth-child(3) { background: linear-gradient(#d9c48a, #bfc3c6); }
  .work-strip__shot:nth-child(4) { background: linear-gradient(#8b5a3a, #c4a88c); }
  .info-band {
    position: absolute; left: 0; top: 368px; width: 445px; height: 72px; background: var(--lilac);
  }
  .info-band .services { left: 30px; top: 10px; font-size: 10.5px; line-height: 14px; }
  .info-band .contact { left: 256px; top: 6px; font-size: 10.5px; line-height: 15px; }
  .info-band .contact__phone { font-size: 17px; line-height: 22px; }
  .side-panel {
    position: absolute; left: 445px; top: 277px; width: 132px; height: 163px;
    background: var(--panel-black); color: var(--panel-text);
  }
  .side-panel .brand { left: 12px; top: 50px; font-size: 10.5px; gap: 5px; letter-spacing: .5px; }
  .side-panel .brand__mark { width: 8px; height: 8px; }
  .side-panel__note {
    position: absolute; left: 14px; top: 78px; width: 110px;
    font-size: 7.5px; line-height: 10px; text-transform: uppercase;
  }
</style>
</head>
<body>

<section class="postcard postcard--back" aria-label="Postcard address side">
  <div class="brand"><span class="brand__mark"></span>Marlow Painting</div>
  <p class="tagline">30 YEARS IN BUSINESS-LICENSED AND INSURED</p>
  <ul class="services">
    <li><svg width="11" height="11" viewBox="0 0 10 10"><rect x=".5" y=".5" width="9" height="9" fill="none" stroke="currentColor"/><path d="M2 5l2 2 4-5" fill="none" stroke="currentColor" stroke-width="1.2"/></svg>All types of painting and staining-house</li>
    <li><svg width="11" height="11" viewBox="0 0 10 10"><rect x=".5" y=".5" width="9" height="9" fill="none" stroke="currentColor"/><path d="M2 5l2 2 4-5" fill="none" stroke="currentColor" stroke-width="1.2"/></svg>Deck and roof powerwashing-stone</li>
    <li><svg width="11" height="11" viewBox="0 0 10 10"><rect x=".5" y=".5" width="9" height="9" fill="none" stroke="currentColor"/><path d="M2 5l2 2 4-5" fill="none" stroke="currentColor" stroke-width="1.2"/></svg>Masonry sealing</li>
  </ul>
  <div class="contact">
    <p>Ray Pettibone</p>
    <p>pettiboneworks@brushmail.example</p>
    <p class="contact__phone">9145820731</p>
  </div>
</section>

<section class="postcard postcard--front" aria-label="Postcard picture side">
  <div class="hero" role="img" aria-label="Photo of a wooden deck with patio chairs beside a shingled house and trees"></div>
  <div class="work-strip">
    <div class="work-strip__shot" role="img" aria-label="Photo of a worker staining a deck"></div>
    <div class="work-strip__shot" role="img" aria-label="Photo of a worker powerwashing a roof"></div>
    <div class="work-strip__shot" role="img" aria-label="Photo of a worker sealing a masonry wall"></div>
    <div class="work-strip__shot" role="img" aria-label="Photo of a painter on a ladder at a house"></div>
  </div>
  <div class="info-band">
    <ul class="services">
      <li><svg width="9" height="9" viewBox="0 0 10 10"><rect x=".5" y=".5" width="9" height="9" fill="none" stroke="currentColor"/><path d="M2 5l2 2 4-5" fill="none" stroke="currentColor" stroke-width="1.2"/></svg>All types of painting and staining-house</li>
      <li><svg width="9" height="9" viewBox="0 0 10 10"><rect x=".5" y=".5" width="9" height="9" fill="none" stroke="currentColor"/><path d="M2 5l2 2 4-5" fill="none" stroke="currentColor" stroke-width="1.2"/></svg>Deck and roof powerwashing-stone</li>
      <li><svg width="9" height="9" viewBox="0 0 10 10"><rect x=".5" y=".5" width="9" height="9" fill="none" stroke="currentColor"/><path d="M2 5l2 2 4-5" fill="none" stroke="currentColor" stroke-width="1.2"/></svg>Masonry sealing</li>
    </ul>
    <div class="contact">
      <p>Ray Pettibone</p>
      <p>pettiboneworks@brushmail.example</p>
      <p class="contact__phone">9145820731</p>
    </div>
  </div>
  <div class="side-panel">
    <div class="brand"><span class="brand__mark"></span>Marlow Painting</div>
    <p class="side-panel__note">30 years in business-<br>licensed and insured</p>
  </div>
</section>

</body>
</html>
```